Tot Petal Product Label for Tear-Free Head-to-Toe Wash

Need a bottle label design for a new line of natural products targeting infants and children. Products are Pediatrician-developed and paraben-free, sulfate-free, fragrance-free, and cruelty-free. Design should be clean and have a high-end feel to it. Will need other product labels in Tot Petal line designed as well in upcoming projects.

Target Market(s)

Newborn to young elementary age children and their parents

Industry/Entity Type

Cosmetics/Beauty

Font styles to use
Other font styles liked:
• Brand fonts are Jost and Sonorous

Colors

Designer to choose colors to be used in the design.

Requirements
Must have
• Tot Petal logo, Pediatrician Developed logo, and a clean high-end feel to it. The label must fit the specialty bottle we will be using (label measurements and diagram will be provided) for the front and back of bottle only (NOT the side labels). It must include our list of ingredients (will provide once designer selected).
Nice to have
• Should stand out on the shelf of other baby products due to it's clean simplicity and high-end feel
Should not have
• too much of a "kiddie" feel to it (targeting the parents not the kids)

```html
<!DOCTYPE html>
<html lang="en">
<head>
<meta charset="utf-8">
<title>Tot Petal – Tear-Free Head-to-Toe Wash Labels</title>
<link rel="stylesheet" href="https://fonts.googleapis.com/css2?family=Jost:wght@500;700;800&family=Arimo:ital,wght@0,400;0,700;1,700&display=swap">
<style>
  :root {
    --page: #ffffff;
    --label: #faf8f5;
    --label-edge: #ece7df;
    --ink: #1f1f1f;
    --gold: #9a7530;
    --white: #ffffff;
  }
  * { box-sizing: border-box; margin: 0; padding: 0; }
  html, body {
    width: 1200px; height: 1200px; overflow: hidden;
    background: var(--page);
  }
  .canvas { position: relative; width: 1200px; height: 1200px; }

  .label {
    position: absolute;
    top: 576px;
    width: 331px;
    height: 477px;
    background: var(--label);
    border: 1px solid var(--label-edge);
    border-radius: 62px 62px 0 0 / 46px 46px 0 0;
    font-family: "Arimo", Arial, sans-serif;
    color: var(--ink);
  }
  .label--front { left: 173px; overflow: hidden; }
  .label--back { left: 700px; }

  /* Front */
  .brand { position: absolute; left: 23px; top: 85px; display: flex; align-items: center; gap: 8px; }
  .brand__dot { width: 47px; height: 47px; border: 2px solid var(--gold); border-radius: 50%; }
  .brand__text { display: flex; flex-direction: column; }
  .brand__name { font-family: "Jost", sans-serif; font-weight: 700; font-size: 18px; color: var(--ink); line-height: 1; }
  .brand__tagline { font-family: "Jost", sans-serif; font-weight: 500; font-size: 5.5px; letter-spacing: 1px; color: var(--ink); margin-top: 4px; }

  .product-title {
    position: absolute; left: 19px; top: 210px; width: 300px;
    font-family: "Jost", sans-serif; font-weight: 800;
    font-size: 33px; line-height: 33px; color: var(--ink);
  }
  .claim-band {
    position: absolute; left: 0; top: 288px;
    width: 277px; height: 27px;
    background: var(--gold); border-radius: 0 14px 14px 0;
    color: var(--white); font-size: 15px; line-height: 27px; padding-left: 19px;
  }
  .badges { position: absolute; left: 16px; top: 340px; display: flex; gap: 11px; }
  .badge {
    width: 53px; height: 53px; border-radius: 50%;
    border: 1.5px dashed var(--ink); opacity: .75;
  }
  .net-weight {
    position: absolute; left: 19px; top: 434px;
    font-weight: 700; font-size: 16.5px; color: var(--gold);
  }

  /* Back */
  .back-copy { position: absolute; left: 44px; top: 79px; width: 242px; }
  .back-copy p {
    font-size: 13.8px; line-height: 17px; text-align: justify;
  }
  .back-copy h2 {
    font-family: "Arimo", Arial, sans-serif;
    font-style: italic; font-weight: 700;
    font-size: 17px; line-height: 20px; color: var(--gold); margin: 6px 0 4px;
  }
  .maker { position: absolute; left: 44px; top: 396px; font-size: 13.8px; line-height: 17px; }
  .maker__lead { font-style: italic; font-weight: 700; color: var(--gold); }
  .seal {
    position: absolute; left: 234px; top: 390px;
    width: 56px; height: 56px; border-radius: 50%;
    border: 1.5px solid var(--gold);
  }
</style>
</head>
<body>
<main class="canvas">

  <section class="label label--front" aria-label="Front label">
    <div class="brand">
      <span class="brand__dot"></span>
      <div class="brand__text">
        <span class="brand__name">Tot Petal</span>
        <span class="brand__tagline">PURE CARE FROM DAY ONE</span>
      </div>
    </div>

    <h1 class="product-title">Tear-Free Head-<br>to-Toe Wash</h1>
    <div class="claim-band">Naturally formulated for delicate skin</div>

    <div class="badges">
      <span class="badge" role="img" aria-label="Paraben free badge"></span>
      <span class="badge" role="img" aria-label="Sulfate free badge"></span>
      <span class="badge" role="img" aria-label="Fragrance free badge"></span>
      <span class="badge" role="img" aria-label="Cruelty free badge"></span>
    </div>

    <p class="net-weight">Net wt: 73 mL/2,43 fl.oz</p>
  </section>

  <section class="label label--back" aria-label="Back label">
    <div class="back-copy">
      <p>A gentle, all-in-one cleanser made with natural ingredients to protect and nourish baby’s delicate hair and skin. Pediatrician-developed and suitable for daily use from newborn onwards.</p>
      <h2>Directions:</h2>
      <p>Dispense a small amount into hands or washcloth. Gently massage into wet hair and skin. Rinse thoroughly. Avoid contact with eyes.</p>
      <h2>Ingredients:</h2>
      <p>Aqua, Glycerin, Decyl Glucoside, Sodium Lauroyl Lactylate, Coco-Glucoside, Glyceryl Oleate, Xanthan Gum, Sodium Benzoate, Citric Acid. (Full list to be finalized.)</p>
    </div>

    <div class="maker">
      <p class="maker__lead">Manufactured for</p>
      <p>Tot Petal Co.</p>
      <p>totpetalcare.com/Made in USA</p>
    </div>

    <span class="seal" role="img" aria-label="Pediatrician developed seal"></span>
  </section>

</main>
</body>
</html>
```